Legislative compliance to home owners, landlords and agents

Logo, business card and stationaly header for a sole trader offering sevices in the UK to home owners, landlords and Letting agents to meet legislation requirement relating to sale and leasing of rental domestic homes. Services offered include Legionella Risk Assessment, Portable Appliance Testing and Energy Performance Certificates. Logo to include depiction of a house and compliance tick list images. Have an existing card with water splash image to reflect water testing, so considering picking up same wave blue. Company name Talvane Property Services. Web www.talvaneps-example.com. email: info@talvaneps-example.com. Address: Glenmorrow, Aberdeen. All three services to be listed. Name as existing card.,

Target Market(s)

UK home owners, landlords, lettings and estate agents

Industry/Entity Type

Property Management

Contact Information for Business Card

Derek Hollingsby CEng, MSoHTF
Address: Glenmorrow, Aberdeen
Web: www.talvaneps-example.com
e-mail info@talvaneps-example.com
Phone: 07921 458 302
Services: Legionella Risk Assessment, Portable Appliance Testing, Energy Performance Certificate

Logo Text

Talvane Property Services

Font styles to use
Sans Serif

Colors

Designer to choose colors to be used in the design.

Requirements
Must have
• Suitable for standard UK business card size 85 mm x 55 mm, with allowance for safety border/ bleed such that colours extend to outside border of card once printed
Nice to have
• Clear font style and layout
• Happy to see images depicting phone, address etc

```html
<!DOCTYPE html>
<html lang="en">
<head>
<meta charset="utf-8">
<title>Talvane Property Services – Business Card Sets</title>
<link href="https://fonts.googleapis.com/css2?family=Open+Sans:ital,wght@0,400;0,700;1,400&display=swap" rel="stylesheet">
<style>
  :root {
    --stage: #262626;
    --card: #ffffff;
    --roof-grey: #e8e8e8;
    --navy: #262a63;
    --ink: #444444;
    --muted: #5a5a5a;
    --rule: #c8c8cc;
    --label: #ffffff;
  }
  * { box-sizing: border-box; margin: 0; padding: 0; }
  html, body { width: 1200px; height: 1200px; overflow: hidden; }
  body {
    background: var(--stage);
    font-family: "Open Sans", Arial, sans-serif;
    position: relative;
  }
  .set-label {
    position: absolute;
    left: 0; width: 1178px;
    text-align: center;
    color: var(--label);
    font-size: 31px;
    font-weight: 400;
    letter-spacing: 0.5px;
  }
  .set-label--one { top: 77px; }
  .set-label--two { top: 621px; }

  .card {
    position: absolute;
    background: var(--card);
    overflow: hidden;
  }
  .card--one { left: 256px; top: 143px; width: 661px; height: 425px; }
  .card--two { left: 251px; top: 690px; width: 666px; height: 429px; }

  .card__roof-art {
    position: absolute;
    left: 0; top: 0; width: 100%;
    background: linear-gradient(180deg, var(--roof-grey) 0%, var(--roof-grey) 70%, #ffffff 100%);
  }
  .card--one .card__roof-art { height: 270px; }
  .card--two .card__roof-art { height: 240px; }

  .card__name {
    position: absolute; left: 0; width: 100%;
    text-align: center;
    color: var(--navy);
    font-weight: 700;
    font-size: 24px;
    letter-spacing: 0.2px;
  }
  .card__credentials {
    position: absolute; left: 0; width: 100%;
    text-align: center;
    color: var(--muted);
    font-size: 15px;
  }
  .card--one .card__name { top: 124px; left: 5px; }
  .card--one .card__credentials { top: 161px; left: 5px; }
  .card--two .card__name { top: 154px; left: 1px; }
  .card--two .card__credentials { top: 191px; left: 1px; }

  .brand {
    position: absolute;
    display: flex; align-items: center; gap: 10px;
    color: var(--navy);
    font-weight: 700;
    font-size: 18px;
    white-space: nowrap;
  }
  .brand__mark { width: 14px; height: 14px; background: var(--navy); }
  .card--one .brand { left: 56px; top: 276px; }
  .card--two .brand { left: 56px; top: 310px; }

  .card__divider {
    position: absolute;
    width: 1px; height: 95px;
    background: #8a8a8a;
  }
  .card--one .card__divider { left: 360px; top: 222px; }
  .card--two .card__divider { left: 362px; top: 256px; }

  .contact {
    position: absolute;
    list-style: none;
    color: var(--ink);
    font-size: 15px;
  }
  .contact__item { display: flex; align-items: center; gap: 6px; height: 23px; }
  .contact__item--gap { margin-top: 8px; }
  .contact__icon { width: 15px; height: 15px; fill: var(--navy); flex: none; }
  .card--one .contact { left: 372px; top: 220px; }
  .card--two .contact { left: 374px; top: 253px; }

  .card__rule {
    position: absolute;
    height: 1px;
    background: var(--rule);
  }
  .card--one .card__rule { left: 35px; width: 592px; top: 335px; }
  .card--two .card__rule { left: 35px; width: 597px; top: 373px; }

  .services {
    position: absolute; left: 0; width: 100%;
    text-align: center;
    font-style: italic;
    color: var(--muted);
    font-size: 14.5px;
    white-space: nowrap;
  }
  .card--one .services { top: 349px; left: 1px; }
  .card--two .services { top: 379px; left: 1px; }
</style>
</head>
<body>

<svg width="0" height="0" style="position:absolute" aria-hidden="true">
  <defs>
    <symbol id="icon-phone" viewBox="0 0 16 16">
      <path d="M1 6c0-2 3-3.5 7-3.5S15 4 15 6v1.2h-3.2V5.6C10.7 5.2 5.3 5.2 4.2 5.6v1.6H1z"/>
      <path d="M4 8h8l2 5.5H2z M6.5 9.3a1.5 1.5 0 1 0 3 0a1.5 1.5 0 1 0-3 0" fill-rule="evenodd"/>
    </symbol>
    <symbol id="icon-mail" viewBox="0 0 16 16">
      <path d="M1 3.5h14v1L8 9 1 4.5z"/>
      <path d="M1 6l7 4.5L15 6v6.5H1z"/>
    </symbol>
    <symbol id="icon-globe" viewBox="0 0 16 16">
      <path d="M8 1a7 7 0 1 0 0 14A7 7 0 1 0 8 1zm0 1.3c.9 0 1.9 1.8 2.2 4.2H5.8C6.1 4.1 7.1 2.3 8 2.3zM2.4 6.5a5.7 5.7 0 0 1 2.7-3.4 9 9 0 0 0-.9 3.4zm9.4 0a9 9 0 0 0-.9-3.4 5.7 5.7 0 0 1 2.7 3.4zM2.4 9.5h1.8a9 9 0 0 0 .9 3.4 5.7 5.7 0 0 1-2.7-3.4zm3.4 0h4.4c-.3 2.4-1.3 4.2-2.2 4.2s-1.9-1.8-2.2-4.2zm6 0h1.8a5.7 5.7 0 0 1-2.7 3.4 9 9 0 0 0 .9-3.4zM2.3 7.5h11.4v1H2.3z"/>
    </symbol>
    <symbol id="icon-home" viewBox="0 0 16 16">
      <path d="M8 1.5 0.8 8h2v6.5h4v-4h2.4v4h4V8h2z"/>
    </symbol>
  </defs>
</svg>

<h2 class="set-label set-label--one">SET_1</h2>

<section class="card card--one" aria-label="Business card, set one">
  <div class="card__roof-art" role="img" aria-label="Faint grey house roof decoration"></div>
  <h1 class="card__name">DEREK HOLLINGSBY</h1>
  <p class="card__credentials">CEng, MSoHTF</p>
  <div class="brand"><span class="brand__mark"></span>Talvane Property Services</div>
  <div class="card__divider"></div>
  <ul class="contact">
    <li class="contact__item"><svg class="contact__icon"><use href="#icon-phone"/></svg>07921 458 302</li>
    <li class="contact__item"><svg class="contact__icon"><use href="#icon-mail"/></svg>info@talvaneps-example.com</li>
    <li class="contact__item contact__item--gap"><svg class="contact__icon"><use href="#icon-globe"/></svg>www.talvaneps-example.com</li>
    <li class="contact__item"><svg class="contact__icon"><use href="#icon-home"/></svg>Glenmorrow, Aberdeen</li>
  </ul>
  <div class="card__rule"></div>
  <p class="services">Legionella Risk Assessment | Portable Appliance Testing | Energy Performance Certificate</p>
</section>

<h2 class="set-label set-label--two">SET_2</h2>

<section class="card card--two" aria-label="Business card, set two">
  <div class="card__roof-art" role="img" aria-label="Faint grey house roof decoration"></div>
  <h1 class="card__name">DEREK HOLLINGSBY</h1>
  <p class="card__credentials">CEng, MSoHTF</p>
  <div class="brand"><span class="brand__mark"></span>Talvane Property Services</div>
  <div class="card__divider"></div>
  <ul class="contact">
    <li class="contact__item"><svg class="contact__icon"><use href="#icon-phone"/></svg>07921 458 302</li>
    <li class="contact__item"><svg class="contact__icon"><use href="#icon-mail"/></svg>info@talvaneps-example.com</li>
    <li class="contact__item contact__item--gap"><svg class="contact__icon"><use href="#icon-globe"/></svg>www.talvaneps-example.com</li>
    <li class="contact__item"><svg class="contact__icon"><use href="#icon-home"/></svg>Glenmorrow, Aberdeen</li>
  </ul>
  <div class="card__rule"></div>
  <p class="services">Legionella Risk Assessment | Portable Appliance Testing | Energy Performance Certificate</p>
</section>

</body>
</html>
```